Lynx Payments Business card refresh

Need a new design of our business card The info is not what is on these cards i sent this for a reference. I can email all the info over
Info would be Colin Hadley Chief LYNX is the title. our new address is 47615 Birchmoor Ln. Westlake Village Ca 93058 Cell number is 805-462-3179 Work number is 855-307-4926 ext 347 Colin@lynxpaysample.com is my email address
Target Market(s)
Merchant Services all businesses that take credit cards
Industry/Entity Type
Merchant Services / Credit Card processing
Contact Information for Business Card
Need a new design of our business card The info is not what is on these cards i sent this for a reference. I can email all the info over Info would be Colin Hadley Chief LYNX is the title. our new address is 47615 Birchmoor Ln. Westlake Village Ca 93058 Cell number is 805-462-3179 Work number is 855-307-4926 ext 347 Colin@lynxpaysample.com is my email address
Requirements
Must have
- My logo and colors from my brand guidelines
Nice to have
- i sent some designs just need a new refresh
Should not have
- nothing specific

```html
<!DOCTYPE html>
<html lang="en">
<head>
<meta charset="utf-8">
<title>Lynx Payments – Business Card</title>
<link rel="stylesheet" href="https://fonts.googleapis.com/css2?family=Lato:wght@400;700;900&display=swap">
<style>
  :root {
    --stage: #1c1d1f;
    --card: #2b2f33;
    --card-edge: #363b40;
    --panel-dark: #141618;
    --steel-light: #b9c6d0;
    --steel-dark: #3a4148;
    --lime: #8dc21f;
    --white: #ffffff;
    --muted: #e9ecee;
  }
  * { box-sizing: border-box; margin: 0; padding: 0; }
  html, body {
    width: 1200px;
    height: 875px;
    overflow: hidden;
    background: var(--stage);
    font-family: "Lato", sans-serif;
  }
  .stage {
    width: 1200px;
    height: 875px;
    display: flex;
    flex-direction: column;
    align-items: center;
    justify-content: center;
    gap: 40px;
  }
  .card {
    position: relative;
    width: 660px;
    height: 377px;
    background: var(--card);
    border-radius: 22px;
    border: 1px solid var(--card-edge);
    box-shadow: 0 18px 40px rgba(0,0,0,.55);
    overflow: hidden;
  }
  /* Front */
  .card--front {
    display: flex;
    align-items: center;
    justify-content: center;
  }
  .brand-name {
    color: var(--lime);
    font-weight: 900;
    font-size: 58px;
    letter-spacing: 6px;
    text-transform: uppercase;
    line-height: 1;
  }
  .brand-name--small {
    font-size: 30px;
    letter-spacing: 3px;
  }
  /* Back */
  .accent {
    position: absolute;
    right: 0;
    top: 0;
    width: 330px;
    height: 377px;
  }
  .card--back .brand-name {
    position: absolute;
    left: 46px;
    top: 70px;
  }
  .contact-list {
    position: absolute;
    left: 46px;
    top: 140px;
    list-style: none;
    color: var(--white);
  }
  .contact-list li {
    display: flex;
    align-items: flex-start;
    gap: 12px;
    margin-bottom: 9px;
    font-size: 17px;
    line-height: 1.25;
  }
  .contact-list li.is-phone { font-size: 22px; font-weight: 700; margin-bottom: 4px; }
  .contact-list .icon {
    width: 16px;
    height: 16px;
    flex: 0 0 16px;
    margin-top: 3px;
    fill: var(--lime);
  }
  .contact-list .is-phone .icon { margin-top: 6px; }
  .person {
    position: absolute;
    right: 36px;
    top: 150px;
    text-align: right;
  }
  .person__name {
    color: var(--lime);
    font-weight: 900;
    font-size: 30px;
    letter-spacing: 1px;
    text-transform: uppercase;
    line-height: 1.1;
  }
  .person__title {
    color: var(--muted);
    font-size: 19px;
    margin-top: 4px;
  }
</style>
</head>
<body>
<main class="stage">
  <section class="card card--front" aria-label="Business card front">
    <div class="brand-name">Lynx Payments</div>
  </section>

  <section class="card card--back" aria-label="Business card back">
    <svg class="accent" viewBox="0 0 330 377" preserveAspectRatio="none" aria-hidden="true">
      <defs>
        <linearGradient id="steel" x1="0" y1="0" x2="0" y2="1">
          <stop offset="0" stop-color="var(--steel-dark)"/>
          <stop offset="1" stop-color="var(--steel-light)"/>
        </linearGradient>
      </defs>
      <polygon points="120,0 330,0 330,377 250,377" fill="var(--panel-dark)"/>
      <polygon points="70,0 110,0 250,377 200,377" fill="url(#steel)"/>
    </svg>

    <div class="brand-name brand-name--small">Lynx Payments</div>

    <div class="person">
      <div class="person__name">Colin Hadley</div>
      <div class="person__title">Chief LYNX</div>
    </div>

    <ul class="contact-list">
      <li>
        <svg class="icon" viewBox="0 0 16 16" aria-hidden="true"><path d="M8 0a5.5 5.5 0 0 0-5.5 5.5C2.5 10 8 16 8 16s5.5-6 5.5-10.5A5.5 5.5 0 0 0 8 0zm0 8a2.4 2.4 0 1 1 0-4.8A2.4 2.4 0 0 1 8 8z"/></svg>
        <span>47615 Birchmoor Ln.<br>Westlake Village Ca 93058</span>
      </li>
      <li class="is-phone">
        <svg class="icon" viewBox="0 0 16 16" aria-hidden="true"><path d="M3.6 1 6 3.8 4.6 5.6a10 10 0 0 0 5.8 5.8L12.2 10 15 12.4 13.5 15C7 15 1 9 1 2.5z"/></svg>
        <span>855-307-4926 ext 347</span>
      </li>
      <li class="is-phone">
        <svg class="icon" viewBox="0 0 16 16" aria-hidden="true"><path d="M4 0h8a1 1 0 0 1 1 1v14a1 1 0 0 1-1 1H4a1 1 0 0 1-1-1V1a1 1 0 0 1 1-1zm1 2v10h6V2zm3 11a1 1 0 1 0 0 2 1 1 0 0 0 0-2z"/></svg>
        <span>805-462-3179</span>
      </li>
      <li>
        <svg class="icon" viewBox="0 0 16 16" aria-hidden="true"><path d="M0 3h16v10H0zm1.5 1.2v.3L8 9l6.5-4.5v-.3z"/></svg>
        <span>Colin@lynxpaysample.com</span>
      </li>
      <li>
        <svg class="icon" viewBox="0 0 16 16" aria-hidden="true"><path d="M8 0a8 8 0 1 0 0 16A8 8 0 0 0 8 0zm0 1.5c.9 0 2 1.9 2.3 5.2H5.7C6 3.4 7.1 1.5 8 1.5zM1.6 8.8h2.6c.1 2 .5 3.7 1.2 4.9A6.5 6.5 0 0 1 1.6 8.8zm0-1.6a6.5 6.5 0 0 1 3.8-4.9c-.7 1.2-1.1 2.900-1.2 4.9zm4.1 1.6h4.6C10 12.1 8.9 14.5 8 14.5s-2-2.4-2.3-5.7zm4.9 4.9c.7-1.2 1.1-2.9 1.2-4.9h2.6a6.5 6.5 0 0 1-3.8 4.9zm1.2-6.5c-.1-2-.5-3.7-1.2-4.9a6.5 6.5 0 0 1 3.8 4.9z"/></svg>
        <span>lynxpaysample.com</span>
      </li>
    </ul>
  </section>
</main>
</body>
</html>
```